Dive Bar/ Pop Culture Bar Adult Nugget Night

Hey guys,
Gareth here from Rusty Clems restaurant in Australia. Im after a poster design for our new Monday Night Special - Adult Nugget Night. - Think crumbed chicken or Beef Schnitzel with different toppings like Philly Cheese steak or Cheese burger smash (aka a parmy).

I'm thinking a plain block blue colour background with a vector image as the main focus - see attached graphics. I would like the poster to be a fun and tongue in cheek and a 80's/90's hip hop vibe and vector image of a nugget "thug life".

The info it has to contain are as follows -
- Adult Nugget Night (title)
- Monday Night
- Price $17
- from 5pm

Toppings
- Philly Cheese Steak
- Cheese burger Smash
- Burnt End Beanz

A little about Rusty Clems
-Rusty Clems came about because we fell in love with the old- skool American south culture of slow cooked soul food, thrown together on big hearty share plates in the backyard and tucked into with the ones you love.

We wanted to bring something different to the coast.

Moody and grungy without losing the soul of why we go out to drink and eat in the first place - to fill our bellies and warm our hearts.

That's why communal eating is at the core of what we do. Low 'n' Slow platters of scrumptious, fall off the bone meat. Sided with delicious dishes of your choice. That quietness that falls on the table as everyone savours the flavours. Laughs as you reach across your mate, to fork that last juicy piece of slow cooked meat that someone else was eyeing off. Washing it all down with hand-crafted beer, or better yet, that top shelf whiskey glistening from the back bar. Finishing off the night with the best kind of dessert.. our famous Sticky Date Espresso Martini!

I have found one image on the net that I like....... don't know if it's useful...

Please reach out for any more info or questions needed

Cheers
Gareth

Target Market(s)

20-40 year old for a funky grudge bar

Industry/Entity Type

Dive Bar, Smokehouse, Bar & Grill

Font styles to use
Other font styles liked:
• Veneer

Colors
0054AA
0677BA
7BADD7
CADEEF
E8F1F8
FFF300
FFF600
FEFA6F
FFFEC7
FFFEE8
F0912C
F2A743
F7CA91
FBE8D2
FDF5EE
EB3D1F
EC4F4E
F09395
F8D3D4
FCEDEE

Requirements
Must have
• Business Name "Rusty Clems" will share Logo in later stages
Nice to have
• Nice bold colours which throw back to 1980/90's pop culture

```html
<!DOCTYPE html>
<html lang="en">
<head>
<meta charset="utf-8">
<title>Adult Nugget Night – Rusty Clems</title>
<link rel="stylesheet" href="https://fonts.googleapis.com/css2?family=Bebas+Neue&family=Quicksand:wght@300&family=Arimo&display=swap">
<style>
  :root {
    --bg: #26876f;
    --pink: #f55bae;
    --ink: #121218;
    --cream: #ebe4c2;
    --nugget-fill: #ebe3e1;
    --nugget-edge: #f79a6e;
    --nugget-depth: #5c4036;
    --crumb: #ffae2b;
    --mint: #79d9b9;
    --topping-orange: #f7a83a;
  }
  * { margin: 0; padding: 0; box-sizing: border-box; }
  html, body { width: 849px; height: 1200px; overflow: hidden; background: var(--bg); }
  .poster { position: relative; width: 849px; height: 1200px; background: var(--bg); overflow: hidden; }

  .brand {
    position: absolute; top: 34px; right: 44px; width: 90px;
    font-family: "Bebas Neue", sans-serif; font-size: 38px; line-height: 0.9;
    color: var(--ink); text-align: center;
  }

  .nugget-art {
    position: absolute; left: 217px; top: 743px; width: 416px; height: 204px;
    background: linear-gradient(160deg, var(--crumb) 60%, #f2efe6 60%);
    border-radius: 40% 60% 55% 45% / 30% 40% 70% 60%;
  }

  .title-line {
    position: absolute; font-family: "Bebas Neue", sans-serif; line-height: 0.8;
    white-space: nowrap; transform-origin: left bottom;
    -webkit-text-stroke: 6px var(--ink); paint-order: stroke fill;
  }
  .title-adult, .title-night {
    color: var(--pink);
    text-shadow: -3px -2px 0 #1f1f24, -6px -4px 0 #1f1f24, -9px -6px 0 #1f1f24, -12px -8px 0 #1f1f24,
      -15px -10px 0 #1f1f24, -18px -12px 0 #1f1f24, -21px -14px 0 #1f1f24, -24px -16px 0 #1f1f24,
      -27px -18px 0 #1f1f24, -30px -20px 0 #1f1f24, -33px -22px 0 #1f1f24, -36px -24px 0 #1f1f24,
      -39px -26px 0 #1f1f24, -42px -28px 0 #1f1f24, -45px -30px 0 #1f1f24, -48px -32px 0 #2a2a30;
  }
  .title-adult { left: 240px; top: 232px; font-size: 250px; transform: skewY(-8deg) scaleX(0.85); }
  .title-night { left: 232px; top: 578px; font-size: 268px; transform: skewY(-8deg) scaleX(0.75); }
  .title-nugget {
    left: 236px; top: 420px; font-size: 215px; color: var(--nugget-fill);
    -webkit-text-stroke: 8px var(--nugget-edge);
    transform: skewY(-8deg) scaleX(0.8);
    text-shadow: -3px -2px 0 var(--nugget-depth), -6px -4px 0 var(--nugget-depth), -9px -6px 0 var(--nugget-depth),
      -12px -8px 0 var(--nugget-depth), -15px -10px 0 var(--nugget-depth), -18px -12px 0 var(--nugget-depth),
      -21px -14px 0 var(--nugget-depth), -24px -16px 0 var(--nugget-depth), -27px -18px 0 var(--nugget-depth),
      -30px -20px 0 var(--nugget-depth), -33px -22px 0 var(--nugget-depth), -36px -24px 0 var(--nugget-depth),
      -39px -26px 0 var(--nugget-depth), -42px -28px 0 var(--nugget-depth), -45px -30px 0 var(--nugget-depth);
  }
  .title-night { z-index: 2; }

  .price-badge { position: absolute; left: 628px; top: 596px; width: 140px; height: 150px; z-index: 3; }
  .price-badge svg { display: block; }

  .info { position: absolute; left: 0; top: 1068px; width: 849px; height: 92px; }
  .info-divider { position: absolute; top: 2px; width: 5px; height: 90px; background: var(--cream); }
  .when-label {
    position: absolute; left: 34px; top: 12px; font-family: "Bebas Neue", sans-serif;
    font-size: 34px; letter-spacing: 2px; color: var(--cream); line-height: 1;
  }
  .when-time {
    position: absolute; left: 32px; top: 44px; font-family: "Bebas Neue", sans-serif;
    font-size: 56px; color: var(--pink); line-height: 1;
  }
  .tagline {
    position: absolute; left: 289px; top: 6px; width: 300px; font-family: "Quicksand", sans-serif;
    font-weight: 300; font-size: 20px; letter-spacing: 1.6px; line-height: 26px; color: var(--cream);
  }
  .toppings-label {
    position: absolute; left: 646px; top: 12px; font-family: "Bebas Neue", sans-serif;
    font-size: 34px; letter-spacing: 2px; color: var(--cream); line-height: 1;
  }
  .toppings-list {
    position: absolute; left: 648px; top: 48px; list-style: none; font-family: "Arimo", sans-serif;
    font-size: 16.5px; line-height: 17px;
  }
  .topping-pink { color: var(--pink); }
  .topping-orange { color: var(--topping-orange); }
</style>
</head>
<body>
<main class="poster">
  <div class="brand">Rusty Clems</div>

  <div class="nugget-art" role="img" aria-label="Illustration of a crumbed chicken nugget"></div>

  <h1 class="title">
    <span class="title-line title-adult">ADULT</span>
    <span class="title-line title-nugget">NUGGET</span>
    <span class="title-line title-night">NIGHT</span>
  </h1>

  <div class="price-badge">
    <svg width="140" height="150" viewBox="0 0 140 150" aria-label="Price $17">
      <ellipse cx="62" cy="62" rx="60" ry="58" fill="#222226"/>
      <ellipse cx="74" cy="84" rx="62" ry="62" fill="var(--mint)" stroke="var(--ink)" stroke-width="3"/>
      <text x="74" y="104" text-anchor="middle" font-family="Bebas Neue, sans-serif" font-size="62"
            fill="#6f6a5e" transform="skewY(-8) translate(-3 12)">$17</text>
      <text x="74" y="104" text-anchor="middle" font-family="Bebas Neue, sans-serif" font-size="62"
            fill="#e6e0cc" transform="skewY(-8) translate(0 10)">$17</text>
    </svg>
  </div>

  <section class="info">
    <p class="when-label">MONDAY NIGHT</p>
    <p class="when-time">5 PM</p>
    <span class="info-divider" style="left:246px"></span>
    <p class="tagline">Moody and grungy without losing the soul of why we go out to drink.</p>
    <span class="info-divider" style="left:596px"></span>
    <p class="toppings-label">TOPPINGS</p>
    <ul class="toppings-list">
      <li class="topping-pink">Philly Cheese Steak</li>
      <li class="topping-orange">Cheese burger Smash</li>
      <li class="topping-pink">Burnt End Beanz</li>
    </ul>
  </section>
</main>
</body>
</html>
```